Web Design Project

Need a web design for a website that provides senior corporate executives with leadership assessment and improvement guidance. The homepage has two purposes- 1) place for users to log in (primary purpose), and 2) marketing of the site.

The company is named Ridgeway 470, and it provides 360 degree leadership assessments for senior executives. In a nutshell, that means a person's co-workers, employees, customers, and bosses fill out a survey on how well the person does his or her job; and we tell him how well he or she is doing and how to improve.

The attached logo (360_logo) should serve as the inspiration for colors, and the website must use the logo. The homepage will mostly be used for logging in, so it should be simple, clean, and professional looking. See attached sketch.pdf for what we have in mind. The sketch is provided merely to give insight. We're not married to it. All text can be latinized jibberish in the design.

There is one important size constraint to keep in mind. The attached file (content_dimensions.pdf) specifies a content area that must be (width x height) 850 x 600 px.

Note that sketch.pdf portrays images, but please note these are merely placeholders. We will use screenshots of our application on the homepage, so any images you use in content area should be examples or suggestions.
Updates

Target Market(s)

Senior business executives from large companies in the manufacturing and energy sectors. Typically males aged 25 and older, white collar, upper class, with advanced degrees in business, engineering, and natural sciences.

Industry/Entity Type

It Company

Requirements
Must have
• See content_dimensions.pdf, which specifies the dimensions of the content area (850x600 px) (w x h). The the gutter and sides can expand beyond that, but the content area must be that specific size.

Note: The login panel must be within the content area.

Must use the attached logo (360_logo.png).
Should not have
• No Flash and no animated gifs. No photos of people.

```html
<!DOCTYPE html>
<html lang="en">
<head>
<meta charset="utf-8">
<title>Ridgeway 470 — Leadership Assessment</title>
<link rel="stylesheet" href="https://fonts.googleapis.com/css2?family=Questrial&family=Roboto:wght@300&display=swap">
<style>
  :root {
    --page-bg: #f5f5f5;
    --panel-bg: #ffffff;
    --panel-fade: #ebebeb;
    --panel-border: #d4d4d4;
    --navy: #034a80;
    --orange: #f7941d;
    --green: #8cc84b;
    --text-dark: #3a3a3a;
    --text-body: #4a4a4a;
    --text-muted: #8a8a8a;
    --logo-grey: #9a9a9a;
    --field-border: #cfcfcf;
  }
  * { margin: 0; padding: 0; box-sizing: border-box; }
  html, body { width: 1200px; height: 795px; overflow: hidden; }
  body {
    background: var(--page-bg);
    font-family: "Questrial", "Century Gothic", sans-serif;
    color: var(--text-body);
    position: relative;
  }
  .abs { position: absolute; }

  /* Header */
  .accent-block { left: 237px; top: 115px; width: 72px; height: 35px; background: var(--orange); }
  .brand { left: 320px; top: 34px; width: 110px; text-align: center; }
  .brand-dot { display: block; width: 90px; height: 90px; margin: 0 auto 6px; border-radius: 50%; background: var(--orange); }
  .brand-name { font-size: 17px; color: var(--logo-grey); white-space: nowrap; }

  .main-nav {
    left: 447px; top: 115px; width: 517px; height: 35px;
    background: var(--navy);
  }
  .main-nav a {
    position: absolute; top: 0; line-height: 35px;
    color: #fff; text-decoration: none; font-size: 17px;
    transform: translateX(-50%); letter-spacing: -0.2px;
  }
  .main-nav .sep { position: absolute; top: 10px; width: 0; height: 16px; border-left: 1px dotted rgba(255,255,255,0.6); }

  /* Panels */
  .panel {
    top: 166px; height: 514px;
    border: 1px solid var(--panel-border);
    background: linear-gradient(to bottom, var(--panel-bg) 0%, var(--panel-bg) 75%, var(--panel-fade) 100%);
  }
  .login-panel { left: 237px; width: 231px; }
  .content-panel { left: 472px; width: 494px; }

  /* Login */
  .login-title {
    left: 254px; top: 186px; width: 200px; height: 29px;
    background: var(--green); color: #fff; font-size: 19px;
    line-height: 29px; padding-left: 11px;
  }
  .field {
    left: 254px; width: 200px; height: 30px;
    border: 1px solid var(--field-border); background: #fff;
    font-family: inherit; font-size: 11px; color: var(--text-muted);
    padding-left: 14px; outline: none;
  }
  .field::placeholder { color: var(--text-muted); }
  .login-btn {
    left: 375px; top: 293px; width: 79px; height: 28px;
    border: none; color: #fff; font-family: inherit; font-size: 16px;
    background: repeating-linear-gradient(135deg, #b0b0b0 0 2px, #c4c4c4 2px 4px);
    border-bottom: 2px solid #9c9c9c;
  }

  /* Content */
  .headline { left: 497px; top: 191px; font-size: 17.5px; color: var(--text-dark); letter-spacing: 0.1px; }
  .subline { left: 497px; top: 212px; font-size: 12.3px; color: var(--orange); }
  .copy { font-size: 10.5px; line-height: 15.3px; color: var(--text-dark); }
  .intro { left: 497px; top: 244px; width: 225px; }
  .intro p + p { margin-top: 13px; line-height: 13.5px; }

  .visual { border-radius: 50%; }
  .sphere-visual {
    left: 763px; top: 243px; width: 176px; height: 152px;
    background: radial-gradient(circle at 45% 40%, #e6edf5 0%, #b9cde0 55%, rgba(200,215,230,0) 72%);
  }

  .feature-title { left: 497px; top: 415px; font-size: 14.6px; color: var(--text-dark); }
  .feature-sub { left: 497px; top: 436px; font-size: 10.5px; color: var(--orange); }
  .feature-copy { left: 497px; top: 453px; width: 445px; line-height: 13px; }

  .chart-visual {
    left: 506px; top: 504px; width: 184px; height: 156px; border-radius: 6px;
    background: linear-gradient(160deg, #dff0cf 0%, #f2f2f2 55%, #e2e2e2 100%);
  }
  .divider { left: 717px; top: 510px; height: 143px; border-left: 1px dotted #a8a8a8; }

  .aside-title { left: 735px; top: 508px; width: 220px; font-size: 14.6px; line-height: 18px; color: var(--text-dark); }
  .aside-copy { left: 735px; top: 559px; width: 215px; line-height: 14.6px; }

  /* Footer */
  .copyright { left: 237px; top: 695px; font-family: "Roboto", sans-serif; font-weight: 300; font-size: 10.8px; color: var(--text-muted); }
  .footer-brand { right: 236px; top: 692px; font-size: 17px; color: var(--logo-grey); }
</style>
</head>
<body>
  <header>
    <div class="abs accent-block"></div>
    <div class="abs brand">
      <span class="brand-dot"></span>
      <span class="brand-name">Ridgeway 470</span>
    </div>
    <nav class="abs main-nav">
      <a href="#" style="left:72px">ABOUT</a>
      <span class="sep" style="left:143px"></span>
      <a href="#" style="left:189px">FAQ</a>
      <span class="sep" style="left:243px"></span>
      <a href="#" style="left:297px">HELP</a>
      <span class="sep" style="left:348px"></span>
      <a href="#" style="left:414px">CONTACT</a>
    </nav>
  </header>

  <aside class="abs panel login-panel"></aside>
  <div class="abs login-title">Login</div>
  <input class="abs field" style="top:220px" type="text" placeholder="Enter Your Login Name">
  <input class="abs field" style="top:256px" type="password" placeholder="Enter Your Password">
  <button class="abs login-btn">Login</button>

  <main class="abs panel content-panel"></main>
  <h1 class="abs headline">PROVIDES SENIOR CORPORATE EXECUTIVES</h1>
  <h2 class="abs subline" style="font-weight:normal">With Leadership Assessment And Improvement Guidance</h2>
  <div class="abs copy intro">
    <p>Lorem ipsum dolor sit amet, consectetuer adipiscing elit, sed diam nonummy nibh euismod tincidunt ut laoreet dolore magna aliquam erat volutpat.</p>
    <p>Ut wisi enim ad minim veniam, quis nostrud exerci tation ullamcorper suscipit lobortis nisl ut aliquip ex ea commodo consequat. Duis autem vel eum iriure dolor in hendrerit in vulputate velit esse molestie consequat, vel illum dolore eu.</p>
  </div>
  <div class="abs visual sphere-visual" role="img" aria-label="Illustration of a sphere built from pale blue tiles"></div>

  <h3 class="abs feature-title" style="font-weight:normal">Lorem ipsum dolor sit amet, consectetuer adipiscing elit</h3>
  <p class="abs feature-sub">sed diam nonummy nibh euismod tincidunt ut laoreet dolore</p>
  <p class="abs copy feature-copy">Ut wisi enim ad minim veniam, quis nostrud exerci tation ullamcorper suscipit lobortis nisl ut aliquip ex ea commodo consequat.</p>

  <div class="abs chart-visual" role="img" aria-label="Illustration of a colourful 3D bar chart with a rising green arrow"></div>
  <div class="abs divider"></div>
  <h3 class="abs aside-title" style="font-weight:normal">Lorem ipsum dolor sit amet, consectetuer adipiscing elit</h3>
  <p class="abs copy aside-copy">Ut wisi enim ad minim veniam, quis nostrud exerci tation ullamcorper suscipit lobortis nisl ut aliquip ex ea commodo consequat. Duis autem vel eum iriure dolor in hendrerit in vulputate velit esse molestie consequat, vel illum dolore eu.</p>

  <footer>
    <p class="abs copyright">© Copyright 2013 Ridgeway 470. All rights reserved.</p>
    <p class="abs footer-brand">Ridgeway 470</p>
  </footer>
</body>
</html>
```